A parent Company needs a website as a leading diversified business in industrial Conglomerates in Af

Tesel Group is a private (Holding) limited liability company incorporated under the Companies Code, 1963 (Act 179) in November, 2013 to following the speedy growth in numbers of its current subsidiaries which has been founded several years ago with an emerging force to become one of the largest and a leading diversified business in industrial Conglomerates in Africa.
The Group which is 100% wholly owned indigenous Ghanaian Company focuses on provision of local, value-added products and services that meet the needs of the African population. The Group is headquartered in Accra, Ghana with interests across a range of sectors in Africa.
We are currently into Food & Beverage, Real Estate Development, Transportation, Health Care, Consumer Products Distribution, Agro Processing, Manufacturing, ICT, Exports & Import, and still counting.
In the next 3 years, we shall announce our ambitions to enter Ghana's largest Oil and Gas industry, playing a strategic role in the petroleum sector with strategic alliances, and help build Ghana's biggest and most important Energy sector in the country.
Inspired by billionaires Ned Forlow, Calvin Drossel, and Ubeni Sorkapa, Tesel Group (Tesel Foundation) is committed to making a name for itself on the philanthropic circuit and has given away privately and still given to the cause to the needy in the society and some specific social causes in Ghana.
The company is managed by a 5 member board and a 2 member advisory experts who are non-board members.
The company has a vision, mission and it is guided by its core values.
We would like to see a designs that is very professional and looks corporate and can attract investors and partners. It must communicate financial safety and growth and must reflect our logo colors.

```html
<!DOCTYPE html>
<html lang="en">
<head>
<meta charset="utf-8">
<title>Tesel Group</title>
<link href="https://fonts.googleapis.com/css2?family=Noto+Sans:wght@400;500&display=swap" rel="stylesheet">
<style>
:root{
  --canvas:#d9e1e5;
  --white:#ffffff;
  --brand-blue:#1a80d0;
  --brand-blue-dark:#0d5fa6;
  --ink:#2b2b2b;
  --muted:#4d4d4d;
  --heading:#35799e;
  --accent-bar:#3d6f86;
  --footer-bar:#4b6e79;
  --rule:#d6dadc;
  --social:#8aa3b0;
}
*{margin:0;padding:0;box-sizing:border-box}
html,body{width:1200px;height:1200px;overflow:hidden}
body{background:var(--canvas);font-family:"Noto Sans",sans-serif;color:var(--ink);position:relative}
.canvas-rule{position:absolute;left:0;right:0;top:948px;height:1px;background:#eef2f4}
.site{position:absolute;left:176px;top:0;width:868px;height:1161px;background:var(--white);box-shadow:0 2px 8px rgba(0,0,0,.25)}
.site > *{position:absolute}
.top-strip{left:0;top:0;width:100%;height:5px;background:var(--brand-blue)}
.brand{left:28px;top:96px;display:flex;align-items:center;gap:10px}
.brand-mark{width:28px;height:28px;border-radius:50%;background:var(--brand-blue)}
.brand-name{font-size:21px;color:#222;letter-spacing:.5px;line-height:1}
.social{left:759px;top:19px;display:flex;gap:4px}
.social span{width:24px;height:24px;border-radius:3px;background:var(--social)}
.nav{left:0;top:118px;width:100%;height:30px}
.nav a{position:absolute;top:0;height:30px;line-height:30px;font-size:14px;color:#3b3b3b;text-decoration:none}
.nav a.active{background:var(--brand-blue);color:var(--white);width:70px;text-align:center;font-weight:500}
.nav .sep{position:absolute;top:0;line-height:30px;font-size:14px;color:#555}
.nav-rule{left:0;top:148px;width:100%;height:4px;background:var(--brand-blue)}
.hero{left:8px;top:161px;width:852px;height:267px;background:linear-gradient(180deg,#d8dadc 0%,#9a9fa5 45%,#3c3f46 80%,#7b6a58 100%)}
.hero-shadow{left:8px;top:428px;width:852px;height:24px;background:radial-gradient(ellipse at top,rgba(0,0,0,.18),rgba(0,0,0,0) 70%)}
.hero-arrow{top:271px;width:27px;height:52px;background:#eceded;box-shadow:0 1px 3px rgba(0,0,0,.25);display:flex;align-items:center;justify-content:center}
.hero-arrow.prev{left:3px}.hero-arrow.next{left:839px}
.welcome-title{left:35px;top:460px;font-size:15.5px;color:var(--heading);font-weight:400}
.welcome-bar{left:39px;top:488px;width:9px;height:55px;background:var(--accent-bar)}
.welcome-text{left:66px;top:492px;width:600px;font-size:14px;line-height:16px;color:var(--muted)}
.read-more{left:738px;top:483px;width:108px;height:37px;background:var(--brand-blue);border:2px solid var(--brand-blue-dark);border-radius:2px;color:var(--white);font-size:14px;line-height:33px;text-align:center}
.section-rule{left:31px;top:560px;width:816px;height:1px;background:var(--rule)}
.verticals-title{left:33px;top:572px;font-size:15.5px;color:var(--heading);font-weight:400}
.tile{width:190px;height:117px;background:linear-gradient(180deg,#e6e8ea,#bfc3c6);border:1px solid #b5b9bc;box-shadow:0 8px 10px -6px rgba(0,0,0,.35)}
.tile-photo{position:absolute;left:7px;top:7px;right:7px;bottom:7px}
.tile-title{position:absolute;left:7px;top:7px;right:7px;min-height:19px;background:rgba(40,40,40,.85);color:var(--white);font-size:13px;line-height:16px;text-align:center;padding:2px 0 1px}
.footer-title{top:961px;font-size:15.5px;color:#333;font-weight:400}
.footer-divider{top:966px;width:1px;height:148px;background:var(--rule)}
.service-list{left:35px;top:992px;width:167px;list-style:none}
.service-list li{font-size:11.5px;color:#333;height:26.3px;line-height:21px;border-bottom:1px solid var(--rule)}
.service-list li:last-child{border-bottom:none}
.post{left:317px;width:420px;height:46px}
.post-thumb{position:absolute;left:0;top:0;width:44px;height:45px;background:linear-gradient(180deg,#4f6f93,#c9a98e 55%,#2a3544)}
.post-text{position:absolute;left:55px;top:0;width:190px;font-size:11.3px;line-height:13px;color:#333}
.post-author{position:absolute;left:185px;top:37px;font-size:11.3px;color:#333}
.contact-row{left:634px;width:167px;border-bottom:1px solid var(--rule);font-size:11.5px;color:#333;line-height:18px}
.contact-row svg{position:absolute;left:7px;top:2px}
.contact-row p{padding-left:29px}
.copyright{left:0;top:1123px;width:100%;height:38px;background:var(--footer-bar);color:var(--white);font-size:11.5px;line-height:38px;text-align:center}
</style>
</head>
<body>
<div class="canvas-rule"></div>
<div class="site">
  <div class="top-strip"></div>

  <div class="brand">
    <div class="brand-mark"></div>
    <div class="brand-name">TESEL GROUP</div>
  </div>

  <div class="social" aria-label="Social links"><span></span><span></span><span></span></div>

  <nav class="nav">
    <a class="active" style="left:387px">Home</a>
    <a style="left:466px">About Us</a><span class="sep" style="left:537px">|</span>
    <a style="left:551px">Services</a><span class="sep" style="left:618px">|</span>
    <a style="left:635px">Clients</a><span class="sep" style="left:692px">|</span>
    <a style="left:704px">Partners</a><span class="sep" style="left:771px">|</span>
    <a style="left:783px">Contact Us</a>
  </nav>
  <div class="nav-rule"></div>

  <div class="hero" role="img" aria-label="Business team in suits meeting around laptops in a bright office"></div>
  <div class="hero-shadow"></div>
  <div class="hero-arrow prev"><svg width="10" height="18" viewBox="0 0 10 18"><path d="M8 1 2 9l6 8" fill="none" stroke="#999" stroke-width="1.5"/></svg></div>
  <div class="hero-arrow next"><svg width="10" height="18" viewBox="0 0 10 18"><path d="M2 1l6 8-6 8" fill="none" stroke="#999" stroke-width="1.5"/></svg></div>

  <h2 class="welcome-title">Welcome to Tesel Group</h2>
  <div class="welcome-bar"></div>
  <p class="welcome-text">The professionals at Tesel Group USA and its customer-facing companies are redefining how our customers and manufacturer partners compete in IT, communications and sustainable-energy markets.</p>
  <div class="read-more">Read More</div>
  <div class="section-rule"></div>

  <h2 class="verticals-title">Feature Business verticals</h2>

  <div class="tile" style="left:30px;top:609px">
    <div class="tile-photo" role="img" aria-label="Plated appetizers in white spoons" style="background:linear-gradient(135deg,#5d6f86,#c9b7a0 50%,#6b4d3a)"></div>
    <div class="tile-title">Food &amp; Beverage</div>
  </div>
  <div class="tile" style="left:329px;top:609px">
    <div class="tile-photo" role="img" aria-label="Hand holding a small model house on green background" style="background:radial-gradient(circle at 50% 50%,#d9d2c6,#5f9a3a 60%,#2f6a1f)"></div>
    <div class="tile-title">Real Estate Development</div>
  </div>
  <div class="tile" style="left:635px;top:609px">
    <div class="tile-photo" role="img" aria-label="White delivery truck on a road under blue sky" style="background:linear-gradient(180deg,#7fa8d6,#dfe4ea 55%,#8d9196)"></div>
    <div class="tile-title">Transportation</div>
  </div>

  <div class="tile" style="left:30px;top:760px">
    <div class="tile-photo" role="img" aria-label="Blue stethoscope on a medical chart" style="background:linear-gradient(135deg,#eef3f8,#b9cde0 50%,#1f5e9a)"></div>
    <div class="tile-title">Health Care</div>
  </div>
  <div class="tile" style="left:329px;top:760px">
    <div class="tile-photo" role="img" aria-label="Distribution network diagram with servers and arrows" style="background:#f4f6f8"></div>
    <div class="tile-title" style="padding-bottom:3px">Consumer Products<br>Distribution</div>
  </div>
  <div class="tile" style="left:635px;top:760px">
    <div class="tile-photo" role="img" aria-label="Packaged food products on a red checked cloth" style="background:linear-gradient(180deg,#8fb6dc,#e2d6c8 45%,#c7453e)"></div>
    <div class="tile-title">Agro Processing</div>
  </div>

  <h3 class="footer-title" style="left:33px">Our Services</h3>
  <ul class="service-list">
    <li>Health Care</li><li>Transportation</li><li>Food &amp; Beverage</li><li>Agro Processing</li><li>Real Estate Development</li>
  </ul>
  <div class="footer-divider" style="left:282px"></div>

  <h3 class="footer-title" style="left:315px">Recent Posts</h3>
  <div class="post" style="top:994px">
    <div class="post-thumb" role="img" aria-label="Portrait of a businessman"></div>
    <p class="post-text">The professionals at Tesel Group<br>USA and its client-facing companiy</p>
    <span class="post-author">- Jhon</span>
  </div>
  <div class="post" style="top:1066px">
    <div class="post-thumb" role="img" aria-label="Portrait of a businessman on the phone" style="background:linear-gradient(180deg,#e6e6e6,#c9a98e 55%,#2d2d2d)"></div>
    <p class="post-text">The professionals at Tesel Group<br>USA and its client-facing companiy</p>
    <span class="post-author">- Jhon</span>
  </div>
  <div class="footer-divider" style="left:593px"></div>

  <h3 class="footer-title" style="left:628px">Contact Us</h3>
  <div class="contact-row" style="top:995px;height:42px">
    <svg width="16" height="13" viewBox="0 0 16 13"><path d="M1 2h9v6H5l-3 3V8H1z" fill="#333"/><path d="M11 4h4v6h-1v2l-2-2H7V9h4z" fill="#555"/></svg>
    <p>+91 2345 678 901<br>&nbsp;(011) 2345 6789</p>
  </div>
  <div class="contact-row" style="top:1042px;height:25px">
    <svg width="16" height="13" viewBox="0 0 16 13"><path d="M1 4 13 1l2 8-12 3z" fill="#333"/><path d="M1 4l8 3 4-6" fill="none" stroke="#fff" stroke-width="1"/></svg>
    <p>info@teselgroup.com</p>
  </div>
  <div class="contact-row" style="top:1074px;height:27px">
    <svg width="12" height="14" viewBox="0 0 12 14"><path d="M6 0a5 5 0 0 1 5 5c0 4-5 9-5 9S1 9 1 5a5 5 0 0 1 5-5z" fill="#333"/><circle cx="6" cy="5" r="1.8" fill="#fff"/></svg>
    <p>USA, UK, CANADA</p>
  </div>

  <footer class="copyright">Copyright © 2014 Tesel Group. All rights reserved</footer>
</div>
</body>
</html>
```